Design mobile friendly real estate and property management company landing page

Design a clean, crisp modern looking landing page that is mobile-friendly (must resize, preferably using bootstrap framework). Landing page will consist of heading with login area, company info, body consists of company description and services, a list of available rental properties with photos, and a footer with additional links and info. Working on updating with text for text areas marked A, B, and C on the layout pdf, but in meantime, lorem ipsum is fine. I can connect events to most buttons, etc. Just need the bootstrap and html functionality set up. Previous company website (which should not be relied upon) is www.kbtq.net This is somewhat of a template for a start, but looking for a more professional and modern design for the new website. But this gives an idea of the content and what needs to be displayed, and how.

Target Market(s)

Clients looking for a property management company that is efficient and well-organized.

Industry/Entity Type

Property Management

Coding

Coded - Design and coding required

Number of Pages Required

1 page

Font styles to use
Sans Serif

Colors
0355a3

Requirements
Must have
• Resize for the screen using bootstrap.
• Navigation that collapses for mobile devices
• Large text boxes and good solid spacing around all elements.
Nice to have
• for property images it would be nice if they can be swiped on touch enabled devices (to the next or previous image). And have navigation that can be clicked to next or previous images.
• Would be nice if a captcha verification was included on contact form.
Should not have
• Fancy or eccentric art

```html
<!DOCTYPE html>
<html lang="en">
<head>
<meta charset="utf-8">
<title>Harbor Crest Realty</title>
<meta name="viewport" content="width=1200">
<link href="https://fonts.googleapis.com/css2?family=Noto+Serif:wght@400;700&family=Open+Sans:wght@400;600;700&display=swap" rel="stylesheet">
<style>
:root{
  --brand:#0355a3;
  --brand-dark:#033f7c;
  --brand-deep:#0b3a78;
  --navy:#101c36;
  --ink:#222a35;
  --muted:#6b7480;
  --line:#dfe3e8;
  --panel:#e9ecf0;
  --white:#ffffff;
}
*{box-sizing:border-box;margin:0;padding:0}
html,body{width:1200px;height:2941px;overflow:hidden}
body{font-family:"Open Sans",Arial,sans-serif;color:var(--ink);background:var(--white);position:relative}
.serif{font-family:"Noto Serif",Georgia,serif}

/* header */
.site-header{position:absolute;top:0;left:0;width:1200px;height:129px;background:var(--white)}
.brand-box{position:absolute;left:114px;top:35px;width:219px;height:59px;background:var(--navy);border:3px double #fff;outline:2px solid var(--navy);display:flex;align-items:center;justify-content:center;color:#fff;font-family:"Noto Serif",Georgia,serif;font-size:19px;letter-spacing:1px}
.search-bar{position:absolute;left:369px;top:43px;width:525px;height:47px;border:1px solid var(--line);border-radius:4px;display:flex;align-items:center;font-size:11px;color:var(--muted);box-shadow:0 1px 4px rgba(0,0,0,.08)}
.search-bar .field{height:100%;display:flex;align-items:center;justify-content:space-between;padding:0 14px;border-right:1px solid var(--line)}
.search-bar .field:nth-child(1){width:135px}
.search-bar .field:nth-child(2),.search-bar .field:nth-child(3),.search-bar .field:nth-child(4){width:112px}
.search-bar .field:nth-child(4){border-right:none}
.search-btn{width:34px;height:28px;margin-left:12px;background:var(--brand);border-radius:3px;display:flex;align-items:center;justify-content:center}
.login-btn{position:absolute;left:921px;top:43px;width:167px;height:49px;background:var(--brand);border-radius:3px;color:#fff;font-family:"Noto Serif",Georgia,serif;font-size:14px;display:flex;align-items:center;justify-content:center;gap:6px}

/* nav */
.main-nav{position:absolute;top:129px;left:0;width:1200px;height:63px;background:linear-gradient(#0a4f98,var(--brand-deep));display:flex;align-items:center;padding-left:159px;gap:0;font-size:12px;color:#fff;letter-spacing:.5px}
.main-nav a{color:#fff;text-decoration:none;display:flex;align-items:center;justify-content:center;height:40px}
.main-nav .active{border:2px solid #fff;border-radius:3px;width:78px}
.nav-item-1{margin-left:60px}.nav-item-2{margin-left:86px}.nav-item-3{margin-left:84px}.nav-item-4{margin-left:100px}.nav-item-5{margin-left:96px}

/* hero */
.hero{position:absolute;top:192px;left:0;width:1200px;height:451px;background:linear-gradient(100deg,#6d5a4b 0%,#a48a70 22%,#c9d3dc 48%,#7fa6c9 70%,#2f6fa7 100%)}
.welcome-card{position:absolute;left:112px;top:274px;width:631px;height:369px;background:var(--white);box-shadow:0 2px 10px rgba(0,0,0,.2)}
.welcome-card h1{height:63px;background:linear-gradient(#0a56a6,var(--brand-dark));color:#fff;font-family:"Noto Serif",Georgia,serif;font-weight:400;font-size:19px;padding:0 28px;display:flex;align-items:center}
.welcome-card .body{padding:24px 30px 0;font-size:11px;line-height:26px;color:#444}
.more-link{margin-top:14px;display:inline-flex;align-items:center;gap:6px;color:var(--brand-dark);font-size:12px;padding-bottom:6px;border-bottom:2px solid var(--brand)}
.contact-box{position:absolute;left:833px;top:270px;width:253px;height:467px;background:#f1f2f4;box-shadow:0 2px 8px rgba(0,0,0,.25);padding:66px 24px 0}
.contact-tab{position:absolute;left:37px;top:0;width:180px;height:48px;background:linear-gradient(#9b9b9b,#777);color:#fff;font-family:"Noto Serif",Georgia,serif;font-size:14px;font-weight:700;letter-spacing:.5px;display:flex;align-items:center;justify-content:center}
.contact-box .input{height:45px;background:#fff;border:1px solid #d6d9de;margin-bottom:9px;font-size:10px;color:#888;padding:0 12px;display:flex;align-items:center}
.contact-box .textarea{height:92px;align-items:flex-start;padding-top:16px}
.send-btn{margin-top:18px;height:44px;margin-left:8px;width:190px;background:linear-gradient(#0a56a6,var(--brand-dark));color:#fff;font-family:"Noto Serif",Georgia,serif;font-size:13px;font-weight:700;display:flex;align-items:center;justify-content:center;gap:6px}

/* badges */
.badges{position:absolute;top:658px;left:104px;display:flex;gap:22px}
.badge{height:76px;background:#f4f5f7;display:flex;align-items:center;justify-content:center}
.badge span{display:block;background:#cfd5dc;border-radius:3px}

/* services */
.services{position:absolute;top:760px;left:0;width:1200px;height:640px;background:linear-gradient(120deg,#1f63ad,#0d4f9c 55%,#1a5ea9)}
.service{position:absolute;top:72px;width:468px;color:#fff}
.service h2{font-family:"Noto Serif",Georgia,serif;font-weight:400;font-size:25px;margin-bottom:18px}
.service .photo{height:251px;border:3px solid #fff;border-radius:3px}
.service p{margin-top:18px;font-size:10.5px;line-height:30px}
.read-more{margin-top:22px;width:141px;height:51px;border:2px solid #fff;border-radius:3px;display:flex;align-items:center;justify-content:center;font-family:"Noto Serif",Georgia,serif;font-size:12px}

/* listings */
.listings-title{position:absolute;top:1448px;left:112px;font-family:"Noto Serif",Georgia,serif;font-weight:400;font-size:25px}
.listing{position:absolute;left:112px;width:976px;height:240px;background:var(--panel)}
.listing .thumb{position:absolute;left:25px;top:27px;width:212px;height:188px;background:#fff;box-shadow:0 1px 3px rgba(0,0,0,.15)}
.thumb .label{height:57px;background:var(--brand);color:#fff;font-family:"Noto Serif",Georgia,serif;font-size:12px;display:flex;align-items:center;justify-content:center}
.thumb .photo{height:131px;position:relative}
.thumb .arrow{position:absolute;bottom:4px;width:20px;height:20px;background:rgba(40,40,40,.75);display:flex;align-items:center;justify-content:center}
.listing .details{position:absolute;left:266px;top:27px;width:682px;height:188px;background:#fff;box-shadow:0 1px 3px rgba(0,0,0,.15)}
.details .bar{height:57px;background:var(--brand);color:#fff;font-family:"Noto Serif",Georgia,serif;font-size:12px;display:flex;align-items:center;padding:0 22px}
.bar .addr{flex:1;display:flex;align-items:center;gap:6px}
.bar .spec{display:flex;align-items:center;gap:6px;margin-left:28px}
.details .grid{position:absolute;top:69px;left:36px;display:grid;grid-template-columns:58px 68px 60px 88px;row-gap:0;font-size:10.5px;line-height:27px;color:#555}
.grid .k{color:#666}
.details .note{position:absolute;top:69px;left:380px;width:290px;padding-left:16px;border-left:1px solid var(--line);font-size:10.5px;line-height:27px;color:#8a9098;height:110px}
.note .more{color:var(--brand-dark);display:flex;align-items:center;gap:5px;font-size:10.5px}

/* pagination */
.pagination{position:absolute;top:2599px;left:112px;display:flex;gap:7px;font-size:11px;color:#555}
.pagination span{height:26px;min-width:24px;padding:0 8px;border:1px solid #d5d9de;display:flex;align-items:center;justify-content:center;background:#fff}
.pagination .current{background:var(--brand-dark);color:#fff;border-color:var(--brand-dark)}
.pagination .wide{padding:0 14px}

/* footer */
.site-footer{position:absolute;top:2669px;left:0;width:1200px;height:193px;background:var(--navy);color:#fff}
.footer-col{position:absolute;top:30px}
.footer-col h3{font-family:"Noto Serif",Georgia,serif;font-weight:400;font-size:16px;margin-bottom:16px}
.footer-col p{font-size:10.5px;line-height:23px;color:#d6dbe5}
.socials{display:flex;gap:10px;margin-top:18px}
.socials span{width:27px;height:27px;border:1px solid #fff;border-radius:50%}
.newsletter{margin-top:18px;width:285px;height:41px;background:#fff;border-radius:3px;display:flex;align-items:center;justify-content:space-between;padding-left:16px;color:#999;font-size:10.5px}
.newsletter .go{width:34px;height:31px;margin-right:5px;background:var(--brand-dark);display:flex;align-items:center;justify-content:center}
.contact-line{display:flex;align-items:center;gap:14px;font-size:10.5px;color:#d6dbe5;margin-bottom:14px}
.contact-line .ico{width:31px;height:31px;border:1px solid #fff;border-radius:50%;display:flex;align-items:center;justify-content:center}
.footer-bottom{position:absolute;top:2862px;left:0;width:1200px;height:79px;background:var(--brand);color:#fff;font-size:10.5px;display:flex;align-items:center;justify-content:space-between;padding:0 112px}
</style>
</head>
<body>

<header class="site-header">
  <div class="brand-box">Harbor Crest Realty</div>
  <div class="search-bar">
    <div class="field">Keywords</div>
    <div class="field">Status <svg width="8" height="5"><path d="M0 0h8L4 5z" fill="#777"/></svg></div>
    <div class="field">Type <svg width="8" height="5"><path d="M0 0h8L4 5z" fill="#777"/></svg></div>
    <div class="field">Price <svg width="8" height="5"><path d="M0 0h8L4 5z" fill="#777"/></svg>
      <span class="search-btn"><svg width="12" height="12" viewBox="0 0 12 12"><circle cx="5" cy="5" r="3.5" fill="none" stroke="#fff" stroke-width="1.6"/><path d="M7.6 7.6L11 11" stroke="#fff" stroke-width="1.8"/></svg></span>
    </div>
  </div>
  <div class="login-btn"><svg width="11" height="12" viewBox="0 0 11 12"><circle cx="5.5" cy="3.2" r="3" fill="#fff"/><path d="M0 12c0-4 2.5-5.5 5.5-5.5S11 8 11 12z" fill="#fff"/></svg>LOGIN HERE</div>
</header>

<nav class="main-nav">
  <a class="active">HOME</a>
  <a class="nav-item-1">FOR RENT</a>
  <a class="nav-item-2">FOR SALE</a>
  <a class="nav-item-3">PROPERTY MANAGEMENT</a>
  <a class="nav-item-4">REAL ESTATE</a>
  <a class="nav-item-5">ABOUT</a>
</nav>

<section class="hero" role="img" aria-label="Resort home with an infinity pool overlooking the sea and palm trees"></section>

<article class="welcome-card">
  <h1>Welcome to Harbor Crest Realty</h1>
  <div class="body">
    <p>Nam consectetur sed augue ac lobortis. Donec fringilla facilisis ligula at maximus. Nulla facilisi. Pellentesque tempus velit nisi. Vivamus porttitor augue dolor. Duis ut risus venenatis, hendrerit nisi ac, auctor ipsum. Aliquam non tellus sem. Maecenas iaculis mi at interdum facilisis. Pellentesque bibendum nisi mauris, et gravida tortor varius sit amet. Cras eu enim dolor.</p>
    <p>Sed sed tellus in lectus porttitor tristique eu id metus. Vivamus vitae ornare nulla. Class aptent taciti sociosqu ad litora torquent per conubia nostra, per inceptos himenaeos. Vestibulum gravida, dolor vel rutrum efficitur, velit ante vestibulum magna, at semper arcu elit a augue.</p>
    <span class="more-link"><svg width="11" height="11" viewBox="0 0 11 11"><circle cx="5.5" cy="5.5" r="5.5" fill="#033f7c"/><path d="M4.3 3l2.5 2.5-2.5 2.5" stroke="#fff" stroke-width="1.4" fill="none"/></svg>More Details</span>
  </div>
</article>

<aside class="contact-box">
  <div class="contact-tab">CONTACT NOW</div>
  <div class="input">Name</div>
  <div class="input">Phone</div>
  <div class="input">Email Address</div>
  <div class="input">Subject Property</div>
  <div class="input textarea">Comments</div>
  <div class="send-btn"><svg width="12" height="12" viewBox="0 0 12 12"><path d="M0 5L12 0 8 12 6 7z" fill="#fff"/></svg>SEND</div>
</aside>

<div class="badges">
  <div class="badge" style="width:150px"><span style="width:120px;height:44px"></span></div>
  <div class="badge" style="width:100px"><span style="width:60px;height:46px"></span></div>
  <div class="badge" style="width:72px"><span style="width:40px;height:40px;border-radius:50%"></span></div>
  <div class="badge" style="width:96px"><span style="width:62px;height:26px"></span></div>
  <div class="badge" style="width:68px"><span style="width:38px;height:34px"></span></div>
</div>

<section class="services">
  <div class="service" style="left:112px">
    <h2>Property Management</h2>
    <div class="photo" role="img" aria-label="Modern brick apartment building with balconies under a blue sky" style="background:linear-gradient(160deg,#3f86d6,#9ec7ef 45%,#9a5a3e 70%,#e8e4dc)"></div>
    <p>Lorem ipsum dolor sit amet, consectetur adipiscing elit. Praesent fermentum auctor sem eu ultric ies. Vestibulum non rhoncus dui. Sed viverra nibh in faucibus lacinia. Etiam vel libero ac felis pulvinar pulvinar. In hac habitasse platea dictumst.</p>
    <div class="read-more">READ MORE</div>
  </div>
  <div class="service" style="left:620px">
    <h2>Real Estate</h2>
    <div class="photo" role="img" aria-label="Hands in a suit holding a small white model house" style="background:linear-gradient(135deg,#2b2f38,#56606e 45%,#e9ecef 75%,#c9d4e0)"></div>
    <p>Donec fringilla facilisis ligula at maximus. Nulla facilisi. Pellentesque tempus velit nisi. Vivamus porttitor augue dolor. Duis ut risus venenatis, hendrerit nisi ac, auctor ipsum. Aliquam non tellus sem. Maecenas iaculis mi at interdum facilisis.</p>
    <div class="read-more">READ MORE</div>
  </div>
</section>

<h2 class="listings-title">Featured Listings</h2>

<!-- listing template repeated -->
<div class="listing" style="top:1515px">
  <div class="thumb"><div class="label">FOR RENT</div>
    <div class="photo" role="img" aria-label="Two-storey stucco townhouse with a parked car" style="background:linear-gradient(#8fb7de,#c7a77a 55%,#7b8a5e)">
      <span class="arrow" style="left:4px"><svg width="6" height="8"><path d="M5 0L1 4l4 4" stroke="#fff" fill="none" stroke-width="1.5"/></svg></span>
      <span class="arrow" style="right:4px"><svg width="6" height="8"><path d="M1 0l4 4-4 4" stroke="#fff" fill="none" stroke-width="1.5"/></svg></span>
    </div></div>
  <div class="details">
    <div class="bar"><span class="addr"><svg width="8" height="11" viewBox="0 0 8 11"><path d="M4 0a4 4 0 014 4c0 3-4 7-4 7S0 7 0 4a4 4 0 014-4z" fill="#fff"/><circle cx="4" cy="4" r="1.4" fill="#0355a3"/></svg>4352 ALDER AVE BAYVIEW, CA 90410</span><span class="spec"><svg width="13" height="9"><path d="M0 0v9M0 6h13v3M3 3h10v3" stroke="#fff" fill="none" stroke-width="1.5"/></svg>2 BEDROOM</span><span class="spec"><svg width="8" height="11"><path d="M0 0h8M0 11h8M1 0l6 11M7 0L1 11" stroke="#fff" stroke-width="1.5"/></svg>1 BATH CONDO</span></div>
    <div class="grid"><span class="k">Rent</span><span>$1,600.00</span><span class="k">Community</span><span>: North Park</span><span class="k">Available</span><span>6/1/2016</span><span class="k">Parking</span><span>: 2 assigned...</span><span class="k">Sqft</span><span>675</span><span class="k">Pets</span><span>: Inquire</span><span class="k">Lease</span><span>12 Months</span><span class="k">Laundry</span><span>: On-Site</span></div>
    <div class="note">Highly upgraded 2BR/1BA condo in gated North Park community. Unit features hardwood flooring, granite counters in kitchen and bathroom...<span class="more"><svg width="9" height="9"><circle cx="4.5" cy="4.5" r="4.5" fill="#033f7c"/><path d="M3.5 2.5l2 2-2 2" stroke="#fff" fill="none"/></svg>More Details</span></div>
  </div>
</div>

<div class="listing" style="top:1783px">
  <div class="thumb"><div class="label">FOR SALE</div>
    <div class="photo" role="img" aria-label="Beige suburban house with a double garage and lawn" style="background:linear-gradient(#a9c8e6,#d8cbb0 55%,#6f9a4e)">
      <span class="arrow" style="left:4px"><svg width="6" height="8"><path d="M5 0L1 4l4 4" stroke="#fff" fill="none" stroke-width="1.5"/></svg></span>
      <span class="arrow" style="right:4px"><svg width="6" height="8"><path d="M1 0l4 4-4 4" stroke="#fff" fill="none" stroke-width="1.5"/></svg></span>
    </div></div>
  <div class="details">
    <div class="bar"><span class="addr"><svg width="8" height="11" viewBox="0 0 8 11"><path d="M4 0a4 4 0 014 4c0 3-4 7-4 7S0 7 0 4a4 4 0 014-4z" fill="#fff"/><circle cx="4" cy="4" r="1.4" fill="#0355a3"/></svg>4352LOREM IPSM, CA 92104</span><span class="spec"><svg width="13" height="9"><path d="M0 0v9M0 6h13v3M3 3h10v3" stroke="#fff" fill="none" stroke-width="1.5"/></svg>2 BEDROOM</span><span class="spec"><svg width="8" height="11"><path d="M0 0h8M0 11h8M1 0l6 11M7 0L1 11" stroke="#fff" stroke-width="1.5"/></svg>1 BATH CONDO</span></div>
    <div class="grid"><span class="k">Rent</span><span>$1,600.00</span><span class="k">Community</span><span>: North Park</span><span class="k">Available</span><span>6/1/2016</span><span class="k">Parking</span><span>: 2 assigned...</span><span class="k">Sqft</span><span>675</span><span class="k">Pets</span><span>: Inquire</span><span class="k">Lease</span><span>12 Months</span><span class="k">Laundry</span><span>: On-Site</span></div>
    <div class="note">Highly upgraded 2BR/1BA condo in gated North Park community. Unit features hardwood flooring, granite counters in kitchen and bathroom...<span class="more"><svg width="9" height="9"><circle cx="4.5" cy="4.5" r="4.5" fill="#033f7c"/><path d="M3.5 2.5l2 2-2 2" stroke="#fff" fill="none"/></svg>More Details</span></div>
  </div>
</div>

<div class="listing" style="top:2051px">
  <div class="thumb"><div class="label">FOR RENT</div>
    <div class="photo" role="img" aria-label="Red brick colonial house on a green lawn" style="background:linear-gradient(#9cc3e8,#a2553e 55%,#5e9140)">
      <span class="arrow" style="left:4px"><svg width="6" height="8"><path d="M5 0L1 4l4 4" stroke="#fff" fill="none" stroke-width="1.5"/></svg></span>
      <span class="arrow" style="right:4px"><svg width="6" height="8"><path d="M1 0l4 4-4 4" stroke="#fff" fill="none" stroke-width="1.5"/></svg></span>
    </div></div>
  <div class="details">
    <div class="bar"><span class="addr"><svg width="8" height="11" viewBox="0 0 8 11"><path d="M4 0a4 4 0 014 4c0 3-4 7-4 7S0 7 0 4a4 4 0 014-4z" fill="#fff"/><circle cx="4" cy="4" r="1.4" fill="#0355a3"/></svg>4352LOREM IPSM, CA 92104</span><span class="spec"><svg width="13" height="9"><path d="M0 0v9M0 6h13v3M3 3h10v3" stroke="#fff" fill="none" stroke-width="1.5"/></svg>2 BEDROOM</span><span class="spec"><svg width="8" height="11"><path d="M0 0h8M0 11h8M1 0l6 11M7 0L1 11" stroke="#fff" stroke-width="1.5"/></svg>1 BATH CONDO</span></div>
    <div class="grid"><span class="k">Rent</span><span>$1,600.00</span><span class="k">Community</span><span>: North Park</span><span class="k">Available</span><span>6/1/2016</span><span class="k">Parking</span><span>: 2 assigned...</span><span class="k">Sqft</span><span>675</span><span class="k">Pets</span><span>: Inquire</span><span class="k">Lease</span><span>12 Months</span><span class="k">Laundry</span><span>: On-Site</span></div>
    <div class="note">Highly upgraded 2BR/1BA condo in gated North Park community. Unit features hardwood flooring, granite counters in kitchen and bathroom...<span class="more"><svg width="9" height="9"><circle cx="4.5" cy="4.5" r="4.5" fill="#033f7c"/><path d="M3.5 2.5l2 2-2 2" stroke="#fff" fill="none"/></svg>More Details</span></div>
  </div>
</div>

<div class="listing" style="top:2319px">
  <div class="thumb"><div class="label">FOR SALE</div>
    <div class="photo" role="img" aria-label="Brick family house with twin garage doors" style="background:linear-gradient(#b5d0ea,#8b4a3a 50%,#57753d)">
      <span class="arrow" style="left:4px"><svg width="6" height="8"><path d="M5 0L1 4l4 4" stroke="#fff" fill="none" stroke-width="1.5"/></svg></span>
      <span class="arrow" style="right:4px"><svg width="6" height="8"><path d="M1 0l4 4-4 4" stroke="#fff" fill="none" stroke-width="1.5"/></svg></span>
    </div></div>
  <div class="details">
    <div class="bar"><span class="addr"><svg width="8" height="11" viewBox="0 0 8 11"><path d="M4 0a4 4 0 014 4c0 3-4 7-4 7S0 7 0 4a4 4 0 014-4z" fill="#fff"/><circle cx="4" cy="4" r="1.4" fill="#0355a3"/></svg>4352 ALDER AVE BAYVIEW, CA 90410</span><span class="spec"><svg width="13" height="9"><path d="M0 0v9M0 6h13v3M3 3h10v3" stroke="#fff" fill="none" stroke-width="1.5"/></svg>2 BEDROOM</span><span class="spec"><svg width="8" height="11"><path d="M0 0h8M0 11h8M1 0l6 11M7 0L1 11" stroke="#fff" stroke-width="1.5"/></svg>1 BATH CONDO</span></div>
    <div class="grid"><span class="k">Rent</span><span>$1,600.00</span><span class="k">Community</span><span>: North Park</span><span class="k">Available</span><span>6/1/2016</span><span class="k">Parking</span><span>: 2 assigned...</span><span class="k">Sqft</span><span>675</span><span class="k">Pets</span><span>: Inquire</span><span class="k">Lease</span><span>12 Months</span><span class="k">Laundry</span><span>: On-Site</span></div>
    <div class="note">Highly upgraded 2BR/1BA condo in gated North Park community. Unit features hardwood flooring, granite counters in kitchen and bathroom...<span class="more"><svg width="9" height="9"><circle cx="4.5" cy="4.5" r="4.5" fill="#033f7c"/><path d="M3.5 2.5l2 2-2 2" stroke="#fff" fill="none"/></svg>More Details</span></div>
  </div>
</div>

<nav class="pagination">
  <span class="wide">Prev</span><span class="current">1</span><span>2</span><span>3</span><span>4</span><span>5</span><span>6</span><span>...</span><span>22</span><span class="wide">Next</span>
</nav>

<footer class="site-footer">
  <div class="footer-col" style="left:112px;width:300px">
    <h3>Connect With Us</h3>
    <p>Lorem ipsum dolor sit amet, consectetur adipiscing elit. Suspend e vitae purus blandit.</p>
    <div class="socials"><span></span><span></span><span></span><span></span><span></span></div>
  </div>
  <div class="footer-col" style="left:480px;width:300px">
    <h3>Newsletter Signup</h3>
    <p>Curabitur imperdiet risus id neque aliquet congue mal esuada et nisi.</p>
    <div class="newsletter">Email Address<span class="go"><svg width="12" height="10"><path d="M0 5h10M6 1l4 4-4 4" stroke="#fff" stroke-width="1.8" fill="none"/></svg></span></div>
  </div>
  <div class="footer-col" style="left:843px;width:260px">
    <h3>Contact Us</h3>
    <div class="contact-line"><span class="ico"><svg width="12" height="12" viewBox="0 0 12 12"><path d="M2 0l2.5 3-1.3 1.6c.8 1.7 2.2 3.1 3.9 3.9L8.7 7.2 12 9.7 10.5 12C5 11.6.4 7 0 1.5z" fill="#fff"/></svg></span>555 014 2290</div>
    <div class="contact-line"><span class="ico"><svg width="9" height="12" viewBox="0 0 8 11"><path d="M4 0a4 4 0 014 4c0 3-4 7-4 7S0 7 0 4a4 4 0 014-4z" fill="#fff"/><circle cx="4" cy="4" r="1.4" fill="#101c36"/></svg></span>1280 Lindell Ave, Bayview, CA 90410</div>
  </div>
</footer>
<div class="footer-bottom"><span>Privacy Policy &nbsp;|&nbsp; Contact Us</span><span>© 2016 Harbor Crest Realty. All Rights Reserved.</span></div>

</body>
</html>
```